Packaging Design for Vanta Core

We require an outstanding packaging design for our Vanta Core brand, which offers hydration electrolyte supplements specifically tailored for athletes and sporty individuals.

Benchmark packaging design from liquora competitor attached. The product packaging contains 20 x 20g sticks of the product.

Target Market

Psychographic: Health-conscious, active lifestyle, values quality, functionality and sustainability.

product description 1:
HYDRATION BOOSTER
Refresh, Replenish, Recharge!

product description 2:
PREMIUM ISOTONIC ELECTROLYTE DRINK
Nutritional Expertise Since 1992.

Existing Logo: to add "since 1992"

Appeal to Target Market: Create a design that resonates with both men and women in the 25-55 age group.

Grafik Design: Develop a visually striking design that grabs attention in online retail environments like Brindle.

Visuals: glass of water (or symbolic) and sticks (powder) just like benchmark brand liquora.

Design Elements
Use colours that are inside the Vanta-Core Logo, attached.
Product will be available in 3 flavours. Lemon=yellow, Orange=orange, Black Currant=purple

Typography: Utilize strong, clean, and modern fonts. Ensure readability and create a sense of strength, endurance and reliability.

The product will be available in 3 flavours: Lemon, Orange and Johannisbeere

We look forward to seeing your creative ideas and innovative designs for our Vanta Core brand packaging.

```html
<!DOCTYPE html>
<html lang="en">
<head>
<meta charset="utf-8">
<title>Vanta Core Hydration Booster – Orange</title>
<link rel="stylesheet" href="https://fonts.googleapis.com/css2?family=Poppins:wght@500;600;700;800&display=swap">
<style>
  :root{
    --bg:#dedede;
    --navy:#233f9a;
    --sun:#ffcb05;
    --lime:#eef000;
    --magenta:#d8186a;
    --flame:#f2401f;
    --orange:#ff6a1e;
    --amber:#ffb23a;
    --white:#ffffff;
    --ink:#1d2a6b;
  }
  *{margin:0;padding:0;box-sizing:border-box}
  html,body{width:1200px;height:1200px;overflow:hidden;background:var(--bg);font-family:"Poppins",sans-serif}
  .canvas{position:relative;width:1200px;height:1200px}
  .pouch{position:absolute;left:218px;top:148px;width:756px;height:910px;overflow:hidden;
    background:linear-gradient(180deg,var(--flame) 30%,var(--orange) 60%,var(--amber) 90%)}
  .pouch-shapes{position:absolute;inset:0}
  .count-badge{position:absolute;left:52px;top:2px;width:86px;height:99px;background:var(--lime);
    color:var(--ink);text-align:center;font-weight:700}
  .count-badge .num{display:block;font-size:52px;line-height:62px;letter-spacing:-2px}
  .count-badge .unit{display:block;font-size:17px;line-height:20px}
  .net-weight{position:absolute;left:52px;top:112px;color:var(--white);font-size:10px;font-weight:500}
  .brand{position:absolute;left:238px;top:92px;display:flex;align-items:center;gap:14px}
  .brand-mark{width:54px;height:54px;border-radius:50%;background:var(--magenta)}
  .brand-name{color:var(--lime);font-weight:800;font-size:60px;line-height:1;letter-spacing:-1px}
  .brand-since{position:absolute;left:492px;top:178px;color:var(--white);font-size:16px;font-weight:500}
  .hero-visual{position:absolute;left:432px;top:330px;width:262px;height:580px;
    background:linear-gradient(180deg,rgba(255,255,255,0) 0%,rgba(255,235,215,.45) 40%,rgba(255,245,235,.7) 75%,rgba(255,200,170,.35) 100%);
    border-radius:6px}
  .headline{position:absolute;left:52px;top:398px;color:var(--white);font-weight:700;font-size:72px;line-height:78px;letter-spacing:-1px}
  .tagline{position:absolute;left:56px;top:548px;color:var(--sun);font-weight:600;font-size:19px;text-transform:uppercase}
  .subhead{position:absolute;left:58px;top:620px;color:var(--white);font-weight:700;font-size:34px;line-height:44px;text-transform:uppercase;letter-spacing:-.5px}
  .benefits{position:absolute;left:58px;top:716px;width:380px;display:flex;flex-wrap:wrap;column-gap:22px;
    color:var(--flame);font-weight:600;font-size:19px;list-style:none}
  .benefits li{display:flex;align-items:center;gap:8px;height:36px;white-space:nowrap}
  .benefits li.row-break{flex-basis:100%}
  .benefits svg{width:18px;height:20px;fill:var(--flame)}
  .flavour-pill{position:absolute;left:279px;top:810px;width:202px;height:40px;border-radius:20px;background:var(--sun);
    color:var(--flame);font-weight:700;font-size:20px;text-align:center;line-height:40px;letter-spacing:1px}
  .claim{position:absolute;left:0;right:0;top:864px;text-align:center;color:var(--white);font-weight:500;font-size:15px;letter-spacing:4px}
</style>
</head>
<body>
<main class="canvas">
  <section class="pouch" aria-label="Vanta Core Hydration Booster pouch, orange flavour">
    <svg class="pouch-shapes" viewBox="0 0 756 910" preserveAspectRatio="none" aria-hidden="true">
      <path d="M0 0H756V244Q388 420 0 232Z" fill="var(--navy)"/>
      <path d="M0 232Q388 420 756 244V262Q388 440 0 252Z" fill="var(--sun)"/>
      <line x1="0" y1="64" x2="756" y2="64" stroke="#0d1640" stroke-width="1.5" stroke-dasharray="6 4"/>
      <rect x="0" y="831" width="756" height="79" fill="var(--flame)"/>
    </svg>

    <div class="count-badge"><span class="num">20</span><span class="unit">STICKS</span></div>
    <div class="net-weight">NET WT 14.1oz / 400g</div>

    <div class="brand">
      <span class="brand-mark"></span>
      <span class="brand-name">Vanta Core</span>
    </div>
    <div class="brand-since">Since 1992</div>

    <div class="hero-visual" role="img" aria-label="Powder pouring from a stick into a glass of water"></div>

    <h1 class="headline">HYDRATION<br>BOOSTER</h1>
    <p class="tagline">Refresh, Replenish &amp; Recharge!</p>
    <h2 class="subhead">Premium Isotonic<br>Electrolyte Drink</h2>

    <ul class="benefits">
      <li><svg viewBox="0 0 20 22"><path d="M12 0L3 13h6l-2 9 10-14h-6z"/></svg>Fast Rehydration</li>
      <li><svg viewBox="0 0 20 22"><path d="M10 22V11C10 5 14 2 19 2 19 8 15 11 10 11 5 11 1 8 1 2 6 2 10 5 10 11z"/></svg>Natural Flavors</li>
      <li class="row-break"><svg viewBox="0 0 20 22"><path d="M7 3h6v6h6v6h-6v6H7v-6H1V9h6z"/></svg>Vitamins &amp; Minerals</li>
    </ul>

    <div class="flavour-pill">ORANGE</div>
    <p class="claim">NUTRITIONAL EXPERTISE SINCE 1992</p>
  </section>
</main>
</body>
</html>
```